Trifold Brochure

This is relatively easy. We already have a trifold made we simply want to update the LOOK to look more like our current website. All content would stay the same the only thing that would change would be the fonts, colors and background images to match the current website.

I have attached a word doc of the old trifold brochure. We would want the content to remain on the same pages of the trifold. Again all you are doing is updating the font, logo, colors and any background images. Please comment with any questions.

This is a 5 day project!

Requirements
Must have
• Logo, colors and fonts to match our current website.
http://www.brackenfieldworks.example/

```html
<!DOCTYPE html>
<html lang="en">
<head>
<meta charset="utf-8">
<title>Brackenfield Structural Works – Trifold Brochure</title>
<link href="https://fonts.googleapis.com/css2?family=Archivo+Black&family=Arimo:wght@400;700&family=Questrial&display=swap" rel="stylesheet">
<style>
  :root{
    --green-dark:#5b7431;
    --green-mid:#6f8a3c;
    --green-light:#b8d089;
    --green-pale:#e6efd6;
    --paper:#ffffff;
    --ink:#1e1e1e;
    --backdrop:#dcdcd8;
  }
  *{box-sizing:border-box;margin:0;padding:0}
  html,body{width:1200px;height:1200px;overflow:hidden;background:var(--backdrop)}
  body{font-family:"Questrial",sans-serif;color:var(--ink);position:relative}

  .brochure{position:absolute;left:50px;top:175px;width:1100px;height:850px;display:flex;box-shadow:0 4px 18px rgba(0,0,0,.18)}
  .panel{width:366.67px;height:100%;position:relative;overflow:hidden}

  /* Who we are */
  .panel--about{background:var(--green-dark);color:#fff;padding:70px 34px 0 34px}
  .about__title{font-family:"Arimo",sans-serif;font-weight:700;font-size:16px;letter-spacing:.5px;margin-bottom:10px}
  .about__text{font-size:12.4px;line-height:1.42;text-align:justify;margin-bottom:16px}
  .about__mark{position:absolute;left:34px;bottom:38px;font-family:"Questrial",sans-serif;font-size:64px;color:rgba(255,255,255,.12)}

  /* Designer's corner */
  .panel--designer,.panel--cover{background:linear-gradient(180deg,#ffffff 0%,#f4f6f1 100%);border-left:1px solid #e2e6dc}
  .panel__band{height:62px;background:linear-gradient(90deg,var(--green-light),#c6da9f)}
  .panel__backdrop{position:absolute;inset:62px 0 0 0;background:linear-gradient(160deg,rgba(230,233,226,.0),rgba(220,224,214,.45))}
  .designer__body{position:relative;padding:26px 30px 0 30px}
  .designer__title{font-family:"Arimo",sans-serif;font-weight:700;color:var(--green-mid);font-size:13.5px;margin-bottom:14px}
  .designer__subtitle{font-family:"Arimo",sans-serif;font-weight:700;font-size:12px;margin-bottom:12px}
  .designer__text{font-size:11.6px;line-height:1.4;text-align:justify;margin-bottom:14px}

  .contact{position:absolute;left:0;right:0;bottom:34px;text-align:center}
  .brand{display:flex;align-items:center;justify-content:center;gap:8px;font-family:"Arimo",sans-serif;font-weight:700;color:var(--green-mid)}
  .brand__dot{width:14px;height:14px;border-radius:50%;background:var(--green-mid)}
  .contact .brand{font-size:13.5px;color:var(--ink);margin-bottom:12px}
  .contact .brand__dot{background:var(--green-mid)}
  .contact__line{font-size:9.5px;line-height:1.35}
  .contact__line b{font-family:"Arimo",sans-serif}

  /* Cover */
  .cover__brand{position:relative;margin-top:80px;font-size:13px;color:var(--ink)}
  .cover__brand .brand__name{font-size:13.5px}
  .cover__headline{position:relative;margin-top:60px;text-align:center;font-family:"Archivo Black",sans-serif;color:var(--green-dark);font-size:25px;line-height:1.27;letter-spacing:.3px}
  .services{position:relative;list-style:none;margin:66px 0 0 100px}
  .service{display:flex;align-items:flex-start;gap:10px;font-family:"Arimo",sans-serif;font-size:11.5px;color:var(--green-mid);text-transform:uppercase;margin-bottom:13px;line-height:1.25}
  .service svg{flex:none;width:18px;height:14px;margin-top:1px}
  .cover__footer{position:absolute;left:0;right:0;bottom:0;height:82px;background:var(--green-dark);border-top:4px solid var(--green-light);color:#fff;font-size:11.4px;line-height:1.35;padding:16px 30px 0 30px}
</style>
</head>
<body>
<main class="brochure">

  <section class="panel panel--about">
    <h2 class="about__title">WHO WE ARE</h2>
    <p class="about__text">Following the devastation of Hurricane Sandy, countless homes along the Northeast Coastline were dislodged from their piling foundations. Some of the pilings were completely destroyed while others subsided. Brackenfield Structural Works, LLC (BSW) was established by a team of Engineers, Designers and Material Specialists that witnessed the destructive aftermath personally. This highly skilled team provided engineering services to home owners along the coast at the initial stage of the aftermath recovery efforts. During this time, the BSW team identified a need for an improved solution.</p>
    <p class="about__text">Traditional options available on the market presented problems for the recovery of homes on pilings that needed to be repaired or raised. Options provided to homeowners had drawbacks. The traditional method includes lifting and moving the home away from the pilings, then drive new pilings, and then move the home back. This alternative presented several problems, such as cost and where to place the house during the reinstallation of the pilings. Simply put there is no room for this option in most cases.</p>
    <p class="about__text">As a result, BSW developed a system which allows the house to be raised without actually moving the home, the Collars installed, and the house reset on the Collars without the expense of moving the house or driving new pilings. This option can be installed in a matter of days with limited space and at a lower construction cost. Please see our technical brief for a review of your options and how our system compares to other methods.</p>
    <div class="about__mark" aria-hidden="true">BSW</div>
  </section>

  <section class="panel panel--designer">
    <div class="panel__band" role="img" aria-label="Light green band with faint structural line pattern"></div>
    <div class="panel__backdrop" role="img" aria-label="Faint grey structural framing line pattern"></div>
    <div class="designer__body">
      <h2 class="designer__title">Designer's Corner:</h2>
      <h3 class="designer__subtitle">Notes to Design Professionals:</h3>
      <p class="designer__text">We have a staff Engineer who can assist you with developing permit plans for submission for approval under Section 104.11 of the IRC. We can provide you with standard details in ACAD format with appropriate construction notes and detailed product specification for use in construction documents.</p>
      <p class="designer__text">When designing using our systems, be sure to understand that our system is simply an extension of the piling, and as such, standard lateral supporting must be considered.</p>
      <p class="designer__text">An inspection of each piling is required by the professional to ensure that the piling is free from alignment deflection of greater than 6 degrees, free from dry rot, damage or other defect.</p>
      <p class="designer__text">Our system can be installed below grade, if there is dry rot on the exposed surface of the pile, dig down into the sand, it is likely the piling below the sand and/or the water table is structurally sound. The BSW system can be used as a splice to remove failed sections of pilings and install new sections.</p>
    </div>
    <div class="contact">
      <div class="brand"><span class="brand__dot"></span><span class="brand__name">Brackenfield Structural Works, LLC</span></div>
      <p class="contact__line">P.O.Box 4418, Alder Ridge, PA 18990-0041</p>
      <p class="contact__line"><b>Tel</b> 555.013.2470 &nbsp;|&nbsp; <b>Fax</b> 555.014.8821</p>
      <p class="contact__line"><b>Email:</b> sales@brackenfieldworks.example</p>
      <p class="contact__line">www.brackenfieldworks.example</p>
    </div>
  </section>

  <section class="panel panel--cover">
    <div class="panel__band" role="img" aria-label="Light green band with faint structural line pattern"></div>
    <div class="panel__backdrop" role="img" aria-label="Faint grey structural framing line pattern"></div>
    <div class="brand cover__brand"><span class="brand__dot"></span><span class="brand__name">Brackenfield Structural Works, LLC</span></div>
    <h1 class="cover__headline">REBUILD SAFER<br>STRONGER<br>BETTER</h1>
    <ul class="services">
      <li class="service">
        <svg viewBox="0 0 18 14" aria-hidden="true"><path d="M1 6 L9 1 L17 6 V13 H1 Z" fill="#6f8a3c"/><rect x="4" y="8" width="10" height="1.2" fill="#fff"/><rect x="4" y="10.5" width="10" height="1.2" fill="#fff"/></svg>
        <span>Raising a structure</span>
      </li>
      <li class="service">
        <svg viewBox="0 0 18 14" aria-hidden="true"><path d="M1 12 H17 M3 12 V6 L9 2 L15 6" fill="none" stroke="#6f8a3c" stroke-width="1.4"/><circle cx="9" cy="8" r="2" fill="none" stroke="#6f8a3c" stroke-width="1.2"/></svg>
        <span>New construction</span>
      </li>
      <li class="service">
        <svg viewBox="0 0 18 14" aria-hidden="true"><rect x="1" y="1" width="16" height="1.6" fill="#6f8a3c"/><rect x="2" y="3" width="2" height="10" fill="#6f8a3c"/><rect x="6.5" y="3" width="2" height="10" fill="#6f8a3c"/><rect x="11" y="3" width="2" height="10" fill="#6f8a3c"/><rect x="15" y="3" width="2" height="10" fill="#6f8a3c"/></svg>
        <span>Piling repairs and<br>extensions</span>
      </li>
    </ul>
    <div class="cover__footer">We provide piling repair systems to allow for cost effective reconstruction and modifications to structures on pilings</div>
  </section>

</main>
</body>
</html>
```